BriarLoom Website Homepage Design

Please provide your idea of homepage for a hosting company. This project is for DESIGN only, no coding.

It must use/combine colors used in logo, clean, modern look.

Homepage must consist of at least 4 sections (example: testimonials, services, and so on. not necesarily all of them). We would like the navigation to be horizontal, but not mandatory.

You can include a preview of services page (optional, not a must).

Number of Pages Required

1 page

Font styles to use
Sans Serif

```html
<!DOCTYPE html>
<html lang="en">
<head>
<meta charset="utf-8">
<title>BriarLoom — Hosting Homepage</title>
<link rel="stylesheet" href="https://fonts.googleapis.com/css2?family=Open+Sans:wght@300;400;600;700;800&display=swap">
<style>
:root{
  --blue:#0a84d6;
  --blue-dark:#0873bb;
  --ink:#3d4350;
  --muted:#9aa0a8;
  --line:#e6e8eb;
  --nav-grey:#a7abb1;
  --btn-grey:#9ea2a8;
  --dark-band:#4a4e57;
  --footer:#4b4f5c;
  --news-bg:#e7f3f9;
  --white:#ffffff;
  --hero-a:#0d1d3a;
  --hero-b:#1b3566;
  --accent:#ff6a3d;
}
*{box-sizing:border-box;margin:0;padding:0}
html,body{width:1200px;height:2989px;overflow:hidden}
body{font-family:"Open Sans",Arial,sans-serif;color:var(--ink);background:var(--white)}
.wrap{width:640px;margin:0 auto;position:relative}

/* header */
.top{height:62px}
.top .wrap{display:flex;justify-content:space-between;align-items:center;height:62px}
.brand{display:flex;align-items:center;gap:8px;font-size:24px;font-weight:700;color:var(--blue);letter-spacing:.5px}
.brand .dot{width:14px;height:14px;border-radius:50%;background:var(--blue)}
.top-links{font-size:8px;color:var(--muted);display:flex;gap:12px;border-bottom:1px solid var(--line);padding:6px 0 6px 40px}
.top-links b{color:var(--ink);font-weight:600}
.nav{height:34px}
.nav ul{list-style:none;display:flex;height:34px;background:var(--nav-grey);width:640px;margin:0 auto}
.nav li{flex:auto;text-align:center;line-height:34px;font-size:7.5px;font-weight:600;color:var(--white);letter-spacing:.4px}
.nav li.active{background:var(--blue)}

/* hero */
.hero{height:440px;position:relative;background:radial-gradient(ellipse at center,var(--hero-b),var(--hero-a) 75%);color:var(--white);text-align:center}
.hero-art{position:absolute;left:50%;top:55px;transform:translateX(-50%);width:240px;height:200px;border-radius:6px;background:linear-gradient(180deg,#3c8fe6,#1d5fc2)}
.hero h1{position:absolute;top:292px;left:0;right:0;font-size:24px;font-weight:800;letter-spacing:.5px}
.hero h2{position:absolute;top:324px;left:0;right:0;font-size:22px;font-weight:300;letter-spacing:.5px}
.dots{position:absolute;top:362px;left:50%;transform:translateX(-50%);display:flex;gap:4px}
.dots span{width:7px;height:7px;border:1px solid #b8c6dd;border-radius:50%}
.dots span.on{border-color:var(--blue)}
.arrow{position:absolute;top:185px;width:32px;height:32px}
.arrow.prev{left:306px}.arrow.next{right:204px}

/* search */
.search{height:68px;background:var(--blue)}
.search .wrap{display:flex;height:68px;font-size:8px;color:var(--white);font-weight:600}
.search .www{width:100px;background:var(--blue-dark);display:flex;align-items:center;justify-content:center}
.search .field{flex:1;display:flex;align-items:center;padding-left:18px}
.search .tld{width:100px;background:var(--blue-dark);display:flex;align-items:center;justify-content:center}
.search .go{width:100px;background:#0866a6;display:flex;align-items:center;justify-content:center;gap:6px}

/* section titles */
.kicker{font-size:10px;font-weight:400;color:var(--muted);text-transform:uppercase;position:relative;padding-top:8px}
.kicker::before{content:"";position:absolute;top:0;left:0;width:12px;height:2px;background:var(--blue)}
.title{font-size:16px;font-weight:800;text-transform:uppercase;color:var(--ink)}

/* benefits */
.benefits{height:470px;padding-top:80px}
.benefits .wrap{padding-left:10px}
.benefit-grid{display:grid;grid-template-columns:repeat(3,1fr);gap:34px 20px;margin-top:20px}
.benefit{display:flex;gap:14px}
.benefit svg{flex:none;width:32px;height:32px}
.benefit h3{font-size:8.5px;font-weight:700;margin-bottom:6px}
.benefit p{font-size:7.5px;line-height:13px;color:var(--muted)}

/* hot */
.hot{height:300px;background:var(--dark-band);color:var(--white);padding-top:70px}
.hot .wrap{display:flex;padding-left:10px}
.hot .kicker{color:var(--white)}.hot .title{color:var(--white)}
.hot-col{width:240px}
.deal{margin-top:16px;width:176px;height:58px;background:var(--white);display:flex;align-items:center;padding:0 12px;gap:6px;color:var(--ink)}
.deal small{display:block;font-size:5.5px;font-weight:700}
.deal strong{font-size:22px;font-weight:800;color:var(--accent);line-height:1}
.deal em{font-style:normal;font-size:6px;line-height:9px}
.deal em b{font-size:8px;font-weight:800;display:block}
.feat-list{display:grid;grid-template-columns:145px 95px;margin-top:14px;font-size:7.5px;row-gap:11px}
.feat-list li{list-style:none}
.feat-list li::before{content:"›";margin-right:6px;font-size:10px}
.btn-view{position:absolute;right:0;top:116px;width:82px;height:26px;background:var(--white);color:var(--blue);font-size:7px;font-weight:700;text-align:center;line-height:26px}

/* hosting */
.hosting{height:560px;padding-top:70px}
.hosting .wrap{padding-left:10px}
.plans{display:grid;grid-template-columns:repeat(4,1fr);gap:14px;margin-top:14px}
.plan{border:1px solid var(--line);height:236px;text-align:center;padding-top:12px}
.price{font-size:20px;color:var(--ink)}.price b{font-size:24px;font-weight:800}
.per{font-size:7px;letter-spacing:.6px}
.plan-name{margin:10px auto 18px;width:90px;height:18px;line-height:18px;background:var(--blue);color:var(--white);font-size:6.5px;font-weight:700}
.plan ul{list-style:none;font-size:7px;color:var(--muted)}
.plan li{padding:5px 0;border-top:1px solid var(--line);margin:0 14px}
.plan li:first-child{border-top:none}
.signup{margin:8px auto 0;width:56px;height:20px;line-height:20px;background:var(--btn-grey);color:var(--white);font-size:6.5px;font-weight:700}

/* testimonials */
.testimonials{height:470px;padding-top:30px}
.testi-grid{display:grid;grid-template-columns:repeat(3,1fr);gap:10px;margin-top:24px}
.testi{border:1px solid #eceff4;height:122px;padding:16px 14px;position:relative}
.testi p{font-size:7.5px;line-height:12.5px;color:var(--muted)}
.person{display:flex;align-items:center;gap:10px;margin-top:20px}
.avatar{width:26px;height:26px;border-radius:50%;background:linear-gradient(#c7ced8,#7d8795)}
.person b{display:block;font-size:8px;font-weight:700}
.person span{font-size:6.5px;color:var(--muted)}
.quote{position:absolute;right:18px;bottom:14px;width:36px;height:28px}

/* newsletter */
.newsletter{height:170px;background:var(--news-bg);padding-top:48px}
.newsletter .wrap{display:flex;align-items:flex-end;padding-left:8px}
.nl-title{width:110px}
.nl-title svg{display:block;margin-bottom:6px}
.nl-form{display:flex;flex:1;height:28px;margin-bottom:2px}
.nl-form .in{flex:1;background:var(--white);font-size:7px;color:var(--muted);display:flex;align-items:center;padding-left:12px}
.nl-form .btn{width:96px;background:var(--btn-grey);color:var(--white);font-size:7px;font-weight:700;display:flex;align-items:center;justify-content:center}

/* footer */
.footer{height:415px;background:var(--footer);color:#c3c7d0;padding-top:52px}
.footer .wrap{display:flex;padding-left:10px}
.footer .brand{color:var(--blue);font-size:20px}
.f-brand{width:170px;padding-top:30px}
.f-brand small{display:block;font-size:7px;margin-top:8px}
.f-col h4{font-size:7px;font-weight:700;color:var(--white);margin-bottom:16px;letter-spacing:.4px}
.f-col{font-size:7px;line-height:15px}
.links{width:160px}
.links div{display:grid;grid-template-columns:76px 76px}
.contact{width:142px}.contact b{color:var(--white);font-weight:600}
.social{display:flex;gap:10px}
.social span{width:12px;height:12px;border-radius:50%;border:1.5px solid #c3c7d0}
</style>
</head>
<body>

<header class="top">
  <div class="wrap">
    <div class="brand"><span class="dot"></span>BriarLoom</div>
    <div class="top-links"><span><b>Support :</b> info@briarloom.com</span><span>Register</span><span>Login</span></div>
  </div>
</header>
<nav class="nav">
  <ul>
    <li class="active">HOME</li><li>ABOUT US</li><li>SERVICE</li><li>HOSTING PLANS</li><li>DOMAIN</li><li>FAQ</li><li>TESTIMONIALS</li><li>BLOG</li><li>SUPPORT</li><li>CONTACT US</li>
  </ul>
</nav>

<section class="hero" role="img" aria-label="Dark blue server room backdrop">
  <div class="hero-art" role="img" aria-label="Illustration of server racks with a person on top and security shields"></div>
  <svg class="arrow prev" viewBox="0 0 32 32"><circle cx="16" cy="16" r="14.5" fill="none" stroke="#fff" stroke-width="1.2"/><path d="M18 11l-5 5 5 5" fill="none" stroke="#fff" stroke-width="1.4"/></svg>
  <svg class="arrow next" viewBox="0 0 32 32"><circle cx="16" cy="16" r="14.5" fill="none" stroke="#fff" stroke-width="1.2"/><path d="M14 11l5 5-5 5" fill="none" stroke="#fff" stroke-width="1.4"/></svg>
  <h1>RELIABLE &amp; FAST RESPOND SERVER</h1>
  <h2>FOR YOUR BUSINESS</h2>
  <div class="dots"><span></span><span></span><span class="on"></span></div>
</section>

<section class="search">
  <div class="wrap">
    <div class="www">WWW.</div>
    <div class="field">Enter Your Domain</div>
    <div class="tld">.com ▾</div>
    <div class="go"><svg width="10" height="10" viewBox="0 0 10 10"><circle cx="4" cy="4" r="3" fill="none" stroke="#fff" stroke-width="1.5"/><path d="M6.2 6.2L9 9" stroke="#fff" stroke-width="1.6"/></svg>Search</div>
  </div>
</section>

<section class="benefits">
  <div class="wrap">
    <div class="kicker">Our</div>
    <div class="title">Benefits</div>
    <div class="benefit-grid">
      <div class="benefit"><svg viewBox="0 0 32 32" fill="none" stroke="#0a84d6" stroke-width="2"><circle cx="16" cy="16" r="12"/><path d="M6 12h20M6 16h20M6 20h20"/></svg><div><h3>99.9% UPTIME</h3><p>Lorem Ipsum is simply dummy text of the printing and typesetting industry. Lorem Ipsum has been.</p></div></div>
      <div class="benefit"><svg viewBox="0 0 32 32" fill="none" stroke="#0a84d6" stroke-width="2"><ellipse cx="13" cy="13" rx="10" ry="7"/><path d="M8 19l-2 5 6-3M22 14c5 1 7 4 5 7l1 4-4-2c-3 1-7 0-8-2"/></svg><div><h3>24/7/365 SUPPORT</h3><p>Lorem Ipsum is simply dummy text of the printing and typesetting industry. Lorem Ipsum has been.</p></div></div>
      <div class="benefit"><svg viewBox="0 0 32 32" fill="none" stroke="#0a84d6" stroke-width="2"><rect x="5" y="7" width="22" height="15" rx="1"/><path d="M2 25h28"/></svg><div><h3>PROTECT YOUR PC</h3><p>Lorem Ipsum is simply dummy text of the printing and typesetting industry. Lorem Ipsum has been.</p></div></div>
      <div class="benefit"><svg viewBox="0 0 32 32" fill="none" stroke="#0a84d6" stroke-width="2"><circle cx="16" cy="16" r="5"/><path d="M16 3v5M16 24v5M3 16h5M24 16h5M7 7l3.5 3.5M21.5 21.5L25 25M25 7l-3.5 3.5M10.5 21.5L7 25"/><circle cx="16" cy="16" r="10"/></svg><div><h3>DNS CONTROL</h3><p>Lorem Ipsum is simply dummy text of the printing and typesetting industry. Lorem Ipsum has been.</p></div></div>
      <div class="benefit"><svg viewBox="0 0 32 32" fill="none" stroke="#0a84d6" stroke-width="2"><rect x="4" y="8" width="24" height="17" rx="1"/><path d="M4 9l12 9 12-9"/></svg><div><h3>DOMAIN TRANSFER</h3><p>Lorem Ipsum is simply dummy text of the printing and typesetting industry. Lorem Ipsum has been.</p></div></div>
      <div class="benefit"><svg viewBox="0 0 32 32" fill="none" stroke="#0a84d6" stroke-width="2"><rect x="8" y="14" width="16" height="14" rx="2"/><path d="M11 14V10a5 5 0 0 1 10 0v4"/></svg><div><h3>100% SECURITY</h3><p>Lorem Ipsum is simply dummy text of the printing and typesetting industry. Lorem Ipsum has been.</p></div></div>
    </div>
  </div>
</section>

<section class="hot">
  <div class="wrap">
    <div class="hot-col">
      <div class="kicker">Now</div>
      <div class="title">What is hot</div>
      <div class="deal"><div><small>GET UP TO</small><strong>50% OFF</strong></div><em>EACH<b>HOSTING</b></em></div>
    </div>
    <div>
      <div class="kicker">Our</div>
      <div class="title">Features</div>
      <ul class="feat-list">
        <li>Lorem Ipsum is simply dummy.</li><li>Specimen book.</li>
        <li>Discovered the undoubtable.</li><li>Lpsum generators.</li>
        <li>Various versions have evolved.</li><li>Sentence structures.</li>
        <li>Suffered alteration in some.</li><li>Embarrassing hidden.</li>
      </ul>
    </div>
    <div class="btn-view">VIEW ALL</div>
  </div>
</section>

<section class="hosting">
  <div class="wrap">
    <div class="kicker">Our</div>
    <div class="title">Hosting</div>
    <div class="plans">
      <div class="plan"><div class="price">$<b>5</b></div><div class="per">PER MONTH</div><div class="plan-name">STANDARD PLAN</div><ul><li>10GB Disk Space</li><li>1TB Bandwidth</li><li>Free DDoS Protection</li><li>Free Daily Backups</li><li>Managed Hosting</li></ul><div class="signup">SIGNUP</div></div>
      <div class="plan"><div class="price">$<b>6</b></div><div class="per">PER MONTH</div><div class="plan-name">ADVANCED PLAN</div><ul><li>10GB Disk Space</li><li>1TB Bandwidth</li><li>Free DDoS Protection</li><li>Free Daily Backups</li><li>Managed Hosting</li></ul><div class="signup">SIGNUP</div></div>
      <div class="plan"><div class="price">$<b>8</b></div><div class="per">PER MONTH</div><div class="plan-name">BUSINESS PLAN</div><ul><li>10GB Disk Space</li><li>1TB Bandwidth</li><li>Free DDoS Protection</li><li>Free Daily Backups</li><li>Managed Hosting</li></ul><div class="signup">SIGNUP</div></div>
      <div class="plan"><div class="price">$<b>9</b></div><div class="per">PER MONTH</div><div class="plan-name">GOLD PLAN</div><ul><li>10GB Disk Space</li><li>1TB Bandwidth</li><li>Free DDoS Protection</li><li>Free Daily Backups</li><li>Managed Hosting</li></ul><div class="signup">SIGNUP</div></div>
    </div>
  </div>
</section>

<section class="testimonials">
  <div class="wrap">
    <div class="kicker">Recent</div>
    <div class="title">Testimonials</div>
    <div class="testi-grid">
      <div class="testi"><p>Lorem Ipsum is simply dummy text of the printing and typesetting industry. Lorem Ipsum has been the industry's</p><div class="person"><div class="avatar" role="img" aria-label="Customer portrait"></div><div><b>MAREN HOLT</b><span>Lorem Ipsum</span></div></div><svg class="quote" viewBox="0 0 36 28" fill="#f1f2f6"><path d="M2 2h13v14l-6 10H4l5-10H2zM20 2h13v14l-6 10h-5l5-10h-7z"/></svg></div>
      <div class="testi"><p>Lorem Ipsum is simply dummy text of the printing and typesetting industry. Lorem Ipsum has been the industry's</p><div class="person"><div class="avatar" role="img" aria-label="Customer portrait"></div><div><b>MAREN HOLT</b><span>Lorem Ipsum</span></div></div><svg class="quote" viewBox="0 0 36 28" fill="#f1f2f6"><path d="M2 2h13v14l-6 10H4l5-10H2zM20 2h13v14l-6 10h-5l5-10h-7z"/></svg></div>
      <div class="testi"><p>Lorem Ipsum is simply dummy text of the printing and typesetting industry. Lorem Ipsum has been the industry's</p><div class="person"><div class="avatar" role="img" aria-label="Customer portrait"></div><div><b>MAREN HOLT</b><span>Lorem Ipsum</span></div></div><svg class="quote" viewBox="0 0 36 28" fill="#f1f2f6"><path d="M2 2h13v14l-6 10H4l5-10H2zM20 2h13v14l-6 10h-5l5-10h-7z"/></svg></div>
    </div>
  </div>
</section>

<section class="newsletter">
  <div class="wrap">
    <div class="nl-title">
      <svg width="14" height="11" viewBox="0 0 14 11" fill="none" stroke="#0a84d6" stroke-width="1.4"><rect x="1" y="1" width="12" height="9"/><path d="M1 1l6 5 6-5"/></svg>
      <div class="kicker" style="padding-top:0">Sign up your</div>
      <div class="title">Newsletter</div>
    </div>
    <div class="nl-form"><div class="in">Enter your domain name</div><div class="btn">SIGN UP NOW</div></div>
  </div>
</section>

<footer class="footer">
  <div class="wrap">
    <div class="f-brand"><div class="brand"><span class="dot"></span>BriarLoom</div><small>2021 © Allright Reserved</small></div>
    <div class="f-col links"><h4>QUICK LINKS</h4><div><span>Home</span><span>Faq</span><span>About Us</span><span>Blog</span><span>Service</span><span>Support</span><span>Hosting plans</span><span>Contact</span><span>Domains</span></div></div>
    <div class="f-col contact"><h4>CONTACT US</h4><div><b>Address :</b> PO Box 4410 Harbor Lane<br>West Ridge 8007<br><b>Email :</b> info@briarloom.com<br><b>Call :</b> (+800) 5550 1234</div></div>
    <div class="f-col"><h4>SOCIAL MEDIA</h4><div class="social"><span></span><span></span><span></span><span></span></div></div>
  </div>
</footer>

</body>
</html>
```